Tidy Tuition Brochure

We offer payment processing and customer service solutions for the parents of Charter schools in the United States.
(More info: http://en.refvaultia.org/wiki/Charter_schools_in_the_United_States )

We have some content and are looking to make an 11x17 back and front design collateral piece. We are also looking for business cards and a 10'x10' trade show booth - separate projects but we can probably use the same designer across both.

Target Market(s)

School Administrators, people who work in school offices, specifically people who work with quickbooks or accounting software for schools.

Industry/Entity Type

Trade

Colors

Designer to choose colors to be used in the design.

Requirements
Must have
• Must have 2-4 pages, maybe 8 pages 1/2 size. It must use most of the content I included.
Nice to have
• I would like photos included - but realize that may not be possible given the space requirement.
Should not have
• Too many fonts, anything that is too glitzy.

```html
<!DOCTYPE html>
<html lang="en">
<head>
<meta charset="utf-8">
<title>Tidy Tuition Brochure</title>
<link href="https://fonts.googleapis.com/css2?family=Raleway:ital,wght@0,400;0,500;0,700;0,800;1,400&display=swap" rel="stylesheet">
<style>
  :root {
    --backdrop: #a4a4a4;
    --paper: #ffffff;
    --brand-blue: #2c5fab;
    --panel-blue: #3264ae;
    --ink: #3a3a3a;
    --ink-soft: #4a4a4a;
    --on-blue: #e8eef8;
    --photo-light: #e9eef2;
    --photo-mid: #b9c6d2;
    --photo-accent: #3d6fc0;
    --art-grey: #dfe4ea;
  }
  * { box-sizing: border-box; margin: 0; padding: 0; }
  html, body { width: 1200px; height: 800px; overflow: hidden; }
  body {
    background: var(--backdrop);
    font-family: "Raleway", sans-serif;
    color: var(--ink);
    position: relative;
  }
  .spread {
    position: absolute;
    left: 40px; top: 30px;
    width: 1120px; height: 740px;
    display: flex;
    box-shadow: 0 6px 18px rgba(0,0,0,.25);
  }
  .page { position: relative; width: 560px; height: 740px; background: var(--paper); overflow: hidden; }

  /* Left page */
  .brand {
    position: absolute; left: 106px; top: 108px;
    display: flex; align-items: center; gap: 10px;
  }
  .brand-square { width: 30px; height: 30px; background: var(--brand-blue); }
  .brand-name { font-weight: 800; font-size: 24px; color: var(--brand-blue); letter-spacing: .5px; }
  .intro-title {
    position: absolute; left: 200px; top: 178px;
    font-weight: 700; font-size: 19px; color: var(--brand-blue);
  }
  .intro-copy {
    position: absolute; left: 190px; top: 207px; width: 320px;
    font-style: italic; font-size: 15px; line-height: 19px; color: var(--ink);
  }
  .office-photo {
    position: absolute; left: 0; top: 300px; width: 560px; height: 440px;
    background: linear-gradient(160deg, var(--photo-light) 0%, var(--photo-mid) 55%, var(--photo-accent) 100%);
  }

  /* Right page */
  .section-title {
    font-weight: 800; font-size: 17px; color: var(--brand-blue); letter-spacing: .3px; text-transform: uppercase;
  }
  .pay-methods { position: absolute; left: 40px; top: 104px; }
  .pay-list { list-style: none; margin-top: 8px; }
  .pay-list li { font-size: 14.5px; line-height: 17.5px; color: var(--ink-soft); }
  .pay-list li::before { content: "• "; }
  .channels-art {
    position: absolute; left: 236px; top: 140px; width: 200px; height: 200px;
    background: var(--art-grey); border-radius: 6px;
  }
  .payment-types {
    position: absolute; left: 0; top: 335px; width: 560px; height: 405px;
    background: var(--panel-blue); color: var(--on-blue);
  }
  .payment-types .section-title { position: absolute; left: 162px; top: 40px; font-size: 18px; color: #fff; }
  .payment-types .lead { position: absolute; left: 162px; top: 72px; font-size: 11.5px; font-weight: 500; color: #fff; }
  .types-col { position: absolute; top: 88px; list-style: none; }
  .types-col li { font-size: 11px; line-height: 14px; padding-left: 8px; text-indent: -8px; }
  .types-col li::before { content: "• "; }
  .types-col.first { left: 166px; width: 136px; }
  .types-col.second { left: 314px; width: 150px; top: 82px; }
  .device-art {
    position: absolute; left: 30px; top: 100px; width: 120px; height: 110px;
    background: rgba(255,255,255,.85); border-radius: 6px;
  }
</style>
</head>
<body>
  <main class="spread">
    <section class="page page-left">
      <div class="brand">
        <span class="brand-square"></span>
        <span class="brand-name">Tidy Tuition</span>
      </div>
      <h2 class="intro-title">Why Tidy Tuition</h2>
      <p class="intro-copy">For over 25 years and with 2500 school customers, Tidy Tuition has continued to earn stellar grades from both parents and school administrators.</p>
      <div class="office-photo" role="img" aria-label="Photo of two professionals working at a bright office desk with a laptop and tablet"></div>
    </section>

    <section class="page page-right">
      <div class="pay-methods">
        <h2 class="section-title">How can they pay?</h2>
        <ul class="pay-list">
          <li>Invoices</li>
          <li>Mobile Payments</li>
          <li>E-Invoices</li>
          <li>Automatic Bank Transfers</li>
          <li>Shopping Cart</li>
          <li>Credit Card Payments</li>
          <li>Donation Handling</li>
          <li>Phone Payments</li>
          <li>In-Person Payments</li>
          <li>Mailed Payments</li>
        </ul>
      </div>
      <div class="channels-art" role="img" aria-label="Illustration of a cloud service connected to phone, tablet, desktop and laptop devices"></div>

      <div class="payment-types">
        <div class="device-art" role="img" aria-label="Illustration of a phone and a card reader held in a hand"></div>
        <h2 class="section-title">What types of payments:</h2>
        <p class="lead">Payments for</p>
        <ul class="types-col first">
          <li>Damages/ Repairs</li>
          <li>Goods/ Services</li>
          <li>Extracurricular/ Non-Curricular Activities</li>
          <li>Activities that Supplement a Class/ Educational Program</li>
          <li>Uniforms/ Personal Athletic Equipment</li>
          <li>Registration / Security Deposits</li>
          <li>Extended Care Hours / Late Pickups</li>
          <li>Supplemental Field Trips</li>
          <li>Voluntary Student Insurance</li>
        </ul>
        <ul class="types-col second">
          <li>Technology Equipment / Musical Instruments</li>
          <li>Lab and Shop Classes</li>
          <li>Student Publications</li>
          <li>Graduation Announcements</li>
          <li>Class Rings</li>
          <li>Post-Secondary Instructional Programs</li>
          <li>Lost and Destroyed Textbooks/Workbooks/ Library Books</li>
          <li>Voluntary Student Insurance</li>
          <li>Donations / Gifts</li>
        </ul>
      </div>
    </section>
  </main>
</body>
</html>
```